HARBOUR LANE DECOR

We need a web design for a new business based in Bonny Hills (NSW). We are a small retail outlet on the Mid North Coast (NSW, Australia) selling home wares, gifts, beach wear, artwork, and hampers etc. We would like to a few different samples if that's not too much trouble (e.g. black and white vs colour, e.g. "beach colours").
We would like the website to communicate that we are an affordable, local (community based) business, with customer satisfaction at the forefront of our mind. We have a strong customer service focus, and in addition to retail sales we are now looking to expand into the online hamper business.
We are open 7 days (except public holidays).
Note: We like the design / layout of the "Cork Pail 'N' Shelf Website" if you would like to compare www.corkpailnshelf.com.au

Industry/Entity Type

Business

```html
<!DOCTYPE html>
<html lang="en">
<head>
<meta charset="utf-8">
<title>Harbour Lane Decor</title>
<link rel="stylesheet" href="https://fonts.googleapis.com/css2?family=Poiret+One&family=Federo&family=Mulish:wght@400;600;700&display=swap">
<style>
:root{
  --coral:#f26b63;
  --mint:#8fd0b2;
  --mint-deep:#79c7a9;
  --sun:#f9c64f;
  --sun-soft:#fdeba0;
  --ink:#2b2b2b;
  --grey:#8a8a8a;
  --grey-soft:#a9a9a9;
  --rule:#e6e6e6;
  --paper:#ffffff;
  --panel:#f8f8f8;
}
*{margin:0;padding:0;box-sizing:border-box}
html,body{width:1200px;height:2314px;overflow:hidden;background:var(--paper)}
body{position:relative;font-family:"Mulish",sans-serif;color:var(--ink)}
.abs{position:absolute}
a{color:inherit;text-decoration:none}

.top-band{left:0;top:0;width:1200px;height:12px;background:linear-gradient(90deg,var(--mint),var(--sun),var(--coral),var(--mint),var(--sun),var(--coral),var(--mint))}

.util-left{left:86px;top:72px;font-size:12px;color:#555;display:flex;border-bottom:1px solid var(--rule);padding-bottom:4px}
.util-left span{padding:0 8px;border-left:1px solid var(--rule)}
.util-left span:first-child{padding-left:8px;border-left:none}
.util-right{right:87px;top:72px;font-size:12px;color:#555;display:flex;align-items:center;border-bottom:1px solid var(--rule);padding-bottom:4px}
.util-right span{padding:0 8px;border-left:1px solid var(--rule);display:flex;align-items:center;gap:4px}
.util-right span:first-child{border-left:none}
.util-right .register{color:var(--sun)}

.brand{left:0;width:1200px;top:30px;text-align:center}
.brand-mark{display:block;width:34px;height:34px;margin:8px auto 14px;background:var(--coral)}
.brand-name{font-family:"Poiret One",sans-serif;font-size:25px;letter-spacing:1px;color:#333;font-weight:400}

.nav{left:86px;top:151px;width:1027px;height:46px;border-top:1px solid var(--sun-soft);display:flex;align-items:center;font-family:"Poiret One",sans-serif;font-size:14px;color:#333;letter-spacing:.5px}
.nav-item{position:absolute;top:0;height:45px;line-height:45px}
.nav-item.active{background:var(--sun-soft);color:var(--coral);left:0;width:145px;text-align:center}
.nav-search{position:absolute;right:0;top:10px}

.hero{left:0;top:197px;width:1200px;height:593px;background:linear-gradient(180deg,#4a4743 0%,#6a625a 45%,#4c4640 100%)}
.hero-badge{left:435px;top:322px;width:330px;height:330px;border-radius:50%;background:rgba(255,255,255,.93);text-align:center}
.hero-badge .new{font-family:"Federo",sans-serif;font-size:34px;color:#333;margin-top:66px}
.hero-badge .rule{width:100px;height:2px;background:#ccc;margin:10px auto 12px}
.hero-badge .collection{font-family:"Federo",sans-serif;font-size:50px;color:var(--coral);letter-spacing:1px}
.hero-badge .see{font-size:19px;color:#444;margin-top:20px}
.hero-arrow{top:440px}

.cats{left:86px;top:790px;width:1027px;height:198px;display:flex}
.cat{position:relative;width:342.3px;height:198px;color:#fff}
.cat-home{background:linear-gradient(90deg,#c98aa3 0%,#7fc6ad 45%,var(--mint-deep) 100%)}
.cat-beach{background:linear-gradient(90deg,#9a6a3e 0%,#2f6f86 45%,#1f4f5d 100%)}
.cat-gift{background:linear-gradient(90deg,#d8b7a6 0%,#a8897c 50%,#6f6a68 100%)}
.cat h3{position:absolute;right:12px;top:20px;font-family:"Federo",sans-serif;font-weight:400;font-size:28px}
.cat p{position:absolute;right:12px;top:74px;width:180px;font-size:12px;line-height:16px;text-align:justify}
.cat .see-all{position:absolute;right:12px;bottom:14px;font-size:17px;display:flex;align-items:center;gap:6px;color:#222}
.cat-beach .see-all,.cat-gift .see-all{color:#fff}

.about{left:0;top:1018px;width:1200px;height:415px;background:var(--panel)}
.about-diamond{left:589px;top:1022px}
.about-photo{left:86px;top:1076px;width:313px;height:313px;border:9px solid var(--coral);background:linear-gradient(135deg,#7c8e7c,#b07a4c 55%,#4a4a3c)}
.about-title{left:416px;top:1070px;font-family:"Poiret One",sans-serif;font-size:36px;color:var(--mint);font-weight:400}
.about-text{left:416px;top:1124px;width:660px;font-size:16px;line-height:33.5px;color:var(--grey-soft)}
.about-more{left:417px;top:1328px;font-size:20px;font-weight:700;display:flex;align-items:center;gap:12px}

.gallery-main{left:86px;top:1433px;width:514px;height:513px;background:linear-gradient(160deg,#9aa3a0,#8a6e50 55%,#b35a3c)}
.gallery-a{left:600px;top:1433px;width:256px;height:257px;background:linear-gradient(160deg,#6b6e6a,#4a4f4e)}
.gallery-a-zoom{left:688px;top:1520px;width:80px;height:80px;background:rgba(255,255,255,.35)}
.gallery-b{left:856px;top:1433px;width:257px;height:257px;background:linear-gradient(160deg,#e5e4dc,#6c8a6f 50%,#b34b3a)}
.gallery-note{left:600px;top:1690px;width:513px;height:256px;text-align:center}
.gallery-note h4{font-family:"Poiret One",sans-serif;font-weight:400;font-size:18px;color:var(--coral);margin-top:54px;letter-spacing:.5px}
.gallery-note p{font-size:16px;line-height:34px;color:var(--grey);width:420px;margin:20px auto 0}

.footer-rule{left:0;top:1990px;width:1200px;height:2px;background:#f4a6a2}
.f-col{top:2013px}
.f-col h5{font-family:"Poiret One",sans-serif;font-weight:400;font-size:19px;color:var(--sun);margin-bottom:22px}
.f-list{list-style:none;font-size:14px;color:#777}
.f-list li{height:29px;display:flex;align-items:center;gap:10px}
.f-list li.strong{color:#444;font-weight:600}
.tri{width:0;height:0;border-left:5px solid var(--coral);border-top:4px solid transparent;border-bottom:4px solid transparent}
.contact-row{display:flex;gap:14px;font-size:14px;line-height:19px;color:#666;margin-bottom:16px}
.news p{font-size:14px;line-height:21px;color:#666;width:200px;margin-bottom:24px}
.news-form{display:flex}
.news-input{width:220px;height:43px;border:1px solid #888;font-size:11px;color:#aaa;padding-left:9px;line-height:41px}
.news-send{width:72px;height:43px;background:var(--mint);color:#fff;font-size:17px;font-weight:600;text-align:center;line-height:43px}

.bottom-rule{left:86px;top:2236px;width:1027px;height:1px;background:var(--sun-soft)}
.copyright{left:86px;top:2267px;font-size:11px;font-weight:600;color:#444}
.social{left:911px;top:2253px;display:flex;gap:10px}
.social span{width:43px;height:43px;display:block}
</style>
</head>
<body>

<div class="abs top-band" role="img" aria-label="Decorative zigzag band in beach colours"></div>

<div class="abs util-left"><span>Inspiration</span><span>Advice</span><span>Store Locator</span></div>

<div class="abs brand">
  <span class="brand-mark"></span>
  <span class="brand-name">HARBOUR LANE DECOR</span>
</div>

<div class="abs util-right">
  <span>Sign in</span>
  <span class="register">Register</span>
  <span>
    <svg width="14" height="12" viewBox="0 0 14 12"><path d="M1 1h2l2 7h7l1-5H4" fill="none" stroke="#555" stroke-width="1.2"/><circle cx="6" cy="10.5" r="1" fill="#555"/><circle cx="11" cy="10.5" r="1" fill="#555"/></svg>
    <svg width="6" height="4" viewBox="0 0 6 4"><path d="M0 0h6L3 4z" fill="#555"/></svg>
  </span>
  <span>Checkout</span>
</div>

<nav class="abs nav">
  <span class="nav-item active">HOME WARES</span>
  <span class="nav-item" style="left:196px">GIFTS</span>
  <span class="nav-item" style="left:278px">BEACH WEAR</span>
  <span class="nav-item" style="left:421px">ARTWORK</span>
  <span class="nav-item" style="left:547px">HAMPER</span>
  <span class="nav-item" style="left:664px">ABOUT US</span>
  <span class="nav-item" style="left:792px">CONTACT US</span>
  <svg class="nav-search" width="28" height="28" viewBox="0 0 28 28"><circle cx="12" cy="12" r="9" fill="none" stroke="#333" stroke-width="2"/><path d="M19 19l7 7" stroke="#333" stroke-width="2.4"/></svg>
</nav>

<div class="abs hero" role="img" aria-label="Shop interior with white cube shelving full of cushions, towels, baskets and homewares"></div>
<svg class="abs hero-arrow" style="left:92px" width="40" height="94" viewBox="0 0 40 94"><path d="M38 2L3 47l35 45" fill="none" stroke="rgba(255,255,255,.75)" stroke-width="2"/></svg>
<svg class="abs hero-arrow" style="left:1068px" width="40" height="94" viewBox="0 0 40 94"><path d="M2 2l35 45L2 92" fill="none" stroke="rgba(255,255,255,.75)" stroke-width="2"/></svg>
<div class="abs hero-badge">
  <div class="new">NEW</div>
  <div class="rule"></div>
  <div class="collection">COLLECTION</div>
  <div class="see">See Now &#8250;</div>
</div>

<section class="abs cats">
  <div class="cat cat-home" role="img" aria-label="Embroidered floral cushions on a mint background">
    <h3>HOMEWARE</h3>
    <p>There are many variations of passages of Lorem Ipsum available but the majority humour.</p>
    <span class="see-all">See All <svg width="13" height="13" viewBox="0 0 13 13"><circle cx="6.5" cy="6.5" r="5.5" fill="none" stroke="currentColor" stroke-width="1.3"/><path d="M5.5 4l2.5 2.5L5.5 9" fill="none" stroke="currentColor" stroke-width="1.3"/></svg></span>
  </div>
  <div class="cat cat-beach" role="img" aria-label="Wooden beach chair and straw hat by the sea">
    <h3>BEACHWARE</h3>
    <p>There are many variations of passages of Lorem Ipsum available but the majority humour.</p>
    <span class="see-all">See All <svg width="13" height="13" viewBox="0 0 13 13"><circle cx="6.5" cy="6.5" r="5.5" fill="none" stroke="currentColor" stroke-width="1.3"/><path d="M5.5 4l2.5 2.5L5.5 9" fill="none" stroke="currentColor" stroke-width="1.3"/></svg></span>
  </div>
  <div class="cat cat-gift" role="img" aria-label="Hands holding a white gift box with a red ribbon">
    <h3>GIFTS</h3>
    <p>There are many variations of passages of Lorem Ipsum available but the majority humour.</p>
    <span class="see-all">See All <svg width="13" height="13" viewBox="0 0 13 13"><circle cx="6.5" cy="6.5" r="5.5" fill="none" stroke="currentColor" stroke-width="1.3"/><path d="M5.5 4l2.5 2.5L5.5 9" fill="none" stroke="currentColor" stroke-width="1.3"/></svg></span>
  </div>
</section>

<section class="abs about"></section>
<svg class="abs about-diamond" width="22" height="22" viewBox="0 0 22 22"><path d="M11 0l11 11-11 11L0 11z" fill="var(--sun)"/></svg>
<div class="abs about-photo" role="img" aria-label="Store corner with painted artworks, a mirror, jugs and bright ceramic plates"></div>
<h2 class="abs about-title">HARBOUR LANE DECOR</h2>
<p class="abs about-text">There are many variations of passages of Lorem Ipsum available but the majority have suffered alteration in some form by injected humour or randomised words which dont look even slightly believable.There are many variations of passages of Lorem Ipsum available, but the majority have suffered alteration in some form, by injected humour, or randomised words which don't look even slightly believable.</p>
<a class="abs about-more">Read More <svg width="20" height="14" viewBox="0 0 20 14"><path d="M0 7h18M12 1l6 6-6 6" fill="none" stroke="#222" stroke-width="2"/></svg></a>

<div class="abs gallery-main" role="img" aria-label="Wall of still-life paintings above yellow jugs and patterned ceramic bowls"></div>
<div class="abs gallery-a" role="img" aria-label="Shelves of folded towels and patterned cushions"></div>
<svg class="abs gallery-a-zoom" viewBox="0 0 80 80"><rect width="80" height="80" fill="rgba(255,255,255,.3)"/><circle cx="36" cy="35" r="15" fill="none" stroke="#fff" stroke-width="3"/><path d="M47 46l12 12" stroke="#fff" stroke-width="3.5"/></svg>
<div class="abs gallery-b" role="img" aria-label="White cube shelving with teal glassware, red canisters and baskets"></div>
<div class="abs gallery-note">
  <h4>LOREM IPSUM DOLOR SIT AMET</h4>
  <p>There are many variations of passages of Lorem Ipsum available but the majority have suffered alteration in some form by injected humour or randomised</p>
</div>

<div class="abs footer-rule"></div>

<div class="abs f-col" style="left:86px">
  <h5>CONTACT US</h5>
  <div class="contact-row">
    <svg width="20" height="24" viewBox="0 0 20 24"><path d="M10 1a7 7 0 0 0-7 7c0 5 7 14 7 14s7-9 7-14a7 7 0 0 0-7-7z" fill="none" stroke="var(--coral)" stroke-width="1.6"/><circle cx="10" cy="8" r="2.5" fill="none" stroke="var(--coral)" stroke-width="1.6"/></svg>
    <span>12 Ocean Drive Bonny Hills<br>NSW 2445 Australia</span>
  </div>
  <div class="contact-row">
    <svg width="22" height="20" viewBox="0 0 22 20"><path d="M2 6c0-3 4-4 9-4s9 1 9 4v2h-5V6H7v2H2z" fill="none" stroke="var(--coral)" stroke-width="1.5"/><rect x="4" y="10" width="14" height="8" rx="1" fill="none" stroke="var(--coral)" stroke-width="1.5"/></svg>
    <span>(02) 6555 0142<br>(02) 6555 0187</span>
  </div>
  <div class="contact-row">
    <svg width="22" height="16" viewBox="0 0 22 16"><rect x="1" y="1" width="20" height="14" fill="none" stroke="var(--coral)" stroke-width="1.5"/><path d="M1 1l10 8 10-8" fill="none" stroke="var(--coral)" stroke-width="1.5"/></svg>
    <span>hello@harbourlanedecor.com</span>
  </div>
</div>

<div class="abs f-col" style="left:415px">
  <h5>QUICK LINKS</h5>
  <ul class="f-list">
    <li class="strong"><i class="tri"></i>Clothing</li>
    <li><i class="tri"></i>Shoes</li>
    <li><i class="tri"></i>Bags</li>
    <li><i class="tri"></i>Accessories</li>
    <li><i class="tri"></i>Jewelry</li>
  </ul>
</div>

<div class="abs f-col" style="left:628px">
  <h5>CATEGORIES</h5>
  <ul class="f-list">
    <li class="strong"><i class="tri"></i>Clothing</li>
    <li><i class="tri"></i>Shoes</li>
    <li><i class="tri"></i>Bags</li>
    <li><i class="tri"></i>Accessories</li>
    <li><i class="tri"></i>Jewelry</li>
  </ul>
</div>

<div class="abs f-col news" style="left:820px">
  <h5>NEWS LETTER</h5>
  <p>Sign up and be the first to know about new goods</p>
  <div class="news-form">
    <div class="news-input">Enter your Email Address</div>
    <div class="news-send">Send</div>
  </div>
</div>

<div class="abs bottom-rule"></div>
<div class="abs copyright">&copy; Harbour Lane Decor Pty Ltd 2014 | Privacy | Terms &amp; Conditions | Sitemap</div>
<div class="abs social" aria-label="Social links">
  <span style="background:#3b5a9a"></span>
  <span style="background:#2a9fd8"></span>
  <span style="background:#1b7bb4"></span>
  <span style="background:#f58220"></span>
</div>

</body>
</html>
```